Business Card Design Project

A double sided business card for presentation to business leaders in corporate.

Target Market(s)

Corporate, business professionals, HR

Industry/Entity Type

Business

Requirements
Must have
• FRONT

Logo

www.brightlanecoaching.com.au

BACK

Mara Pollen-Drew
Director

+ 61 (0) 418 536 204
mara@brightlanecoaching.com.au
www.brightlanecoaching.com.au

Impact through energy and employee engagement

("ripples" of logo, bottom corner)

Must be:
- double sided
size: 86 x 54mm
supplied as one pdf with crop marks shown (+- 1mm, with 2-3 mm bleed)

```html
<!DOCTYPE html>
<html lang="en">
<head>
<meta charset="utf-8">
<title>Brightlane Coaching – Business Card</title>
<link href="https://fonts.googleapis.com/css2?family=Questrial&display=swap" rel="stylesheet">
<style>
  :root {
    --plum: #7e2c6a;
    --plum-light: #93437f;
    --plum-dark: #661a53;
    --slate: #4a4a4a;
    --ink-soft: #6b6558;
    --paper: #ffffff;
    --stage-dark: #000000;
    --stage-light: #5e5e5e;
  }
  * { margin: 0; padding: 0; box-sizing: border-box; }
  html, body { width: 1200px; height: 900px; overflow: hidden; }
  body {
    position: relative;
    background: linear-gradient(150deg, var(--stage-dark) 15%, var(--stage-light) 100%);
    font-family: "Questrial", "Century Gothic", sans-serif;
  }
  .card {
    position: absolute;
    background: var(--paper);
    overflow: hidden;
    box-shadow: 3px 4px 8px rgba(0,0,0,0.55);
  }
  .card--front { left: 20px; top: 245px; width: 569px; height: 356px; }
  .card--back  { left: 611px; top: 245px; width: 570px; height: 358px; }

  .front-art { position: absolute; inset: 0; }

  .wordmark {
    position: absolute;
    color: var(--plum);
    line-height: 0.95;
    display: flex;
    align-items: center;
  }
  .wordmark__dot {
    flex: none;
    border-radius: 50%;
    background: var(--plum);
  }
  .wordmark--front { left: 238px; top: 118px; font-size: 54px; gap: 16px; }
  .wordmark--front .wordmark__dot { width: 30px; height: 30px; }
  .wordmark--back { left: 10px; top: 268px; font-size: 27px; gap: 8px; }
  .wordmark--back .wordmark__dot { width: 14px; height: 14px; }

  .front-url {
    position: absolute;
    left: 10px; bottom: 8px;
    color: var(--paper);
    font-size: 19px;
    letter-spacing: 0.2px;
  }

  .back-block {
    position: absolute;
    left: 0; top: 0;
    width: 192px; height: 237px;
    background: linear-gradient(170deg, var(--plum-dark) 0%, var(--plum-light) 100%);
  }
  .back-edge {
    position: absolute;
    right: 0; top: 238px;
    width: 14px; height: 120px;
    background: var(--plum);
  }
  .contact-name {
    position: absolute;
    right: 21px; top: 122px;
    text-align: right;
  }
  .contact-name__name { color: var(--plum); font-size: 24px; letter-spacing: 0.3px; }
  .contact-name__role { color: var(--slate); font-size: 18px; margin-top: 1px; }

  .contact-details {
    position: absolute;
    right: 23px; top: 289px;
    text-align: right;
    color: var(--ink-soft);
    list-style: none;
    line-height: 20px;
  }
  .contact-details__phone { font-size: 19px; }
  .contact-details__email,
  .contact-details__web { font-size: 16px; }
</style>
</head>
<body>
  <section class="card card--front" aria-label="Card front">
    <svg class="front-art" width="569" height="356" viewBox="0 0 569 356" aria-hidden="true">
      <defs>
        <linearGradient id="frontPlum" x1="0" y1="0" x2="0.6" y2="1">
          <stop offset="0" stop-color="#93437f"/>
          <stop offset="0.6" stop-color="#8a3a76"/>
          <stop offset="1" stop-color="#661a53"/>
        </linearGradient>
      </defs>
      <rect width="569" height="356" fill="url(#frontPlum)"/>
      <path d="M228 0 C175 110 185 270 310 356 L569 356 L569 0 Z" fill="#555555"/>
      <path d="M250 0 C196 105 205 265 332 356 L569 356 L569 0 Z" fill="#ffffff"/>
    </svg>
    <div class="wordmark wordmark--front">
      <span class="wordmark__dot"></span>
      <span class="wordmark__text">brightlane<br>coaching</span>
    </div>
    <p class="front-url">www.brightlanecoaching.com.au</p>
  </section>

  <section class="card card--back" aria-label="Card back">
    <div class="back-block"></div>
    <div class="back-edge"></div>
    <div class="contact-name">
      <p class="contact-name__name">Mara Pollen-Drew</p>
      <p class="contact-name__role">Director</p>
    </div>
    <div class="wordmark wordmark--back">
      <span class="wordmark__dot"></span>
      <span class="wordmark__text">brightlane<br>coaching</span>
    </div>
    <ul class="contact-details">
      <li class="contact-details__phone">+ 61 (0) 418 536 204</li>
      <li class="contact-details__email">mara@brightlanecoaching.com.au</li>
      <li class="contact-details__web">www.brightlanecoaching.com.au</li>
    </ul>
  </section>
</body>
</html>
```